Brisk Ladle - menu design and website design ( updated brief ) 19.3.16

We are a small meal health meals made fresh to order business.
We need a menu designed and website design.
We would like the menu to be either bifold or trifold.
Kraft stock will be used to print . We have our own logo can be taken from files attached
We don't currently have any photos but stock photos or place holders are fine, will replace them when we get our own photos.
Or
We are happy to use vintage style illustrations such as a steak, fish, chicken and vegetables.
. We are open to sugestions and ideas but would really like it to stand out as its our selling point.
We have an attached file with most of the info needed.
Need to add a section for chicken black bean stirfry, beef black bean stirfry, teriyaki beef or chicken stirfry, chicken risotto.

Target Market(s)
Time poor, gym people, tradies, healthy meals. fresh, deilivered
Industry/Entity Type
Health
Number of Pages Required
5+ page
Requirements
Must have
- *menu, Kraft stock as background to represent the Kraft it will be printed on.
- * website selectable menu (chose your own) eg. chose your protein source - chicken, fish etc, then chose whats carb source, brown rice, basmati rice etc
- FAQ page, choose which size meal - either 400g meals or 300g meals etc which would take you to different pages which then you can select carb source for each meal etc
- link from FB?

Nice to have
- *menu vintage style illustrations for some foods.
- * website -Payment gateway? Postcode checker. ( web design )

```html
<!DOCTYPE html>
<html lang="en">
<head>
<meta charset="utf-8">
<title>Brisk Ladle – Trifold Menu</title>
<link rel="stylesheet" href="https://fonts.googleapis.com/css2?family=Cinzel:wght@600;700&family=Crimson+Text:wght@400;600;700&family=Dancing+Script:wght@600&display=swap">
<style>
  :root {
    --stage: #6e7176;
    --kraft: #cdbd98;
    --kraft-light: #d8caa8;
    --kraft-dark: #bfae88;
    --ink: #1e1c1a;
    --navy: #1d2c66;
    --green: #178a3c;
    --script-green: #2b8e3e;
    --red: #c2203c;
    --magenta: #a0217c;
    --brown: #6a411d;
    --fold: rgba(90, 70, 40, 0.18);
  }
  * { box-sizing: border-box; margin: 0; padding: 0; }
  html, body { width: 842px; height: 1200px; overflow: hidden; }
  body {
    background: var(--stage);
    font-family: "Crimson Text", Georgia, serif;
    color: var(--ink);
    position: relative;
  }
  .sheet {
    position: absolute;
    left: 31px;
    width: 780px;
    height: 560px;
    background: radial-gradient(ellipse at 40% 35%, var(--kraft-light), var(--kraft) 60%, var(--kraft-dark));
    display: flex;
    overflow: hidden;
    box-shadow: 0 8px 22px rgba(0,0,0,0.35);
  }
  .sheet--outside { top: 26px; }
  .sheet--inside { top: 614px; }
  .panel {
    position: relative;
    width: 260px;
    height: 560px;
    overflow: hidden;
  }
  .panel + .panel { border-left: 1px solid var(--fold); }

  /* shared */
  .photo { position: absolute; border-radius: 50%; }
  .photo--ringed { border: 5px solid var(--navy); }
  .photo--light { border: 4px solid #ffffff; box-shadow: 0 0 0 2px #4aa8d8; }
  .brand {
    display: flex; align-items: center; justify-content: center; gap: 8px;
    font-family: "Crimson Text", Georgia, serif;
    font-weight: 700;
    color: var(--navy);
    text-transform: uppercase;
    letter-spacing: 1px;
  }
  .brand__dot { border-radius: 50%; background: var(--navy); flex: none; }

  /* about */
  .about { padding: 28px 22px 0 24px; }
  .about__title {
    font-family: "Cinzel", Georgia, serif; font-weight: 700;
    font-size: 17px; color: var(--navy); margin-bottom: 12px;
  }
  .about p { font-size: 10.5px; line-height: 1.42; margin-bottom: 9px; }

  /* contacts */
  .contacts__photo {
    width: 220px; height: 220px; left: 20px; top: -18px;
    background: radial-gradient(circle at 45% 60%, #c98f45, #a8692c 55%, #e9dcc6 80%);
  }
  .contacts__brand { position: absolute; top: 214px; left: 0; right: 0; font-size: 17px; }
  .contacts__brand .brand__dot { width: 14px; height: 14px; }
  .contacts__title {
    position: absolute; top: 276px; width: 100%; text-align: center;
    font-family: "Cinzel", Georgia, serif; font-weight: 700; font-size: 17px;
  }
  .contacts__list {
    position: absolute; top: 310px; width: 100%; list-style: none;
    text-align: center; font-size: 13.5px; line-height: 1.55;
  }

  /* cover */
  .cover__brand { position: absolute; top: 92px; left: 0; right: 0; font-size: 22px; }
  .cover__brand .brand__dot { width: 18px; height: 18px; }
  .cover__tagline {
    position: absolute; top: 200px; width: 100%; text-align: center;
    font-family: "Dancing Script", cursive; font-weight: 600; font-size: 30px; color: var(--navy);
  }
  .cover__tagline em { font-style: normal; color: var(--script-green); }
  .cover__photo { position: absolute; left: 0; top: 250px; }

  /* menu */
  .band {
    position: absolute; left: 0; right: 0; height: 32px;
    display: flex; align-items: center; padding-left: 20px;
    font-family: "Cinzel", Georgia, serif; font-weight: 700; font-size: 12.5px;
    color: #ffffff; letter-spacing: 0.3px;
  }
  .band--navy { background: var(--navy); }
  .band--brown { background: var(--brown); }
  .band--green { background: var(--green); }
  .band--red { background: var(--red); }
  .band--magenta { background: var(--magenta); }
  .prices {
    position: absolute; left: 22px; right: 24px; list-style: none;
    font-size: 13px; line-height: 1.38;
  }
  .prices li { display: flex; justify-content: space-between; }
  .flavours {
    position: absolute; left: 22px; right: 18px; list-style: none;
    columns: 2; column-gap: 16px; font-size: 13px; line-height: 1.38;
  }
  .steps-title {
    position: absolute; top: 40px; left: 198px; width: 380px; text-align: center;
    font-family: "Cinzel", Georgia, serif; font-weight: 700; font-size: 17px; color: var(--navy);
    z-index: 2;
  }
  .delivery {
    position: absolute; top: 330px; left: 22px; right: 14px;
    font-family: "Cinzel", Georgia, serif; font-weight: 700; line-height: 1.25;
  }
  .delivery__head { font-size: 16px; }
  .delivery__call { font-size: 11px; }
  .delivery__phone { font-size: 18px; }
</style>
</head>
<body>

<!-- Outside of the trifold -->
<section class="sheet sheet--outside" aria-label="Menu outside">
  <article class="panel about">
    <h2 class="about__title">ABOUT US</h2>
    <p>Brisk Ladle is a family owned and operated business. From humble beginnings in my own home kitchen, cooking meals to reach my training goals, I learned how hard it was to prepare fresh, interesting food every day. So I decided to cook for others too, from a commercial kitchen with the help of a trained chef.</p>
    <p>All our meals are made fresh daily from locally grown produce and cooked to order, never frozen. You choose the protein, carb and vegetables to suit your needs.</p>
    <p>Proteins are weighed cooked: 200g for men and 150g for women. Carbohydrates are 200g for men and 150g for women.</p>
    <p>So from our kitchen to yours, every meal is prepared fresh and with care. Theo, Brisk Ladle Cook</p>
  </article>

  <article class="panel contacts">
    <div class="photo photo--ringed contacts__photo" role="img" aria-label="Photo of crumbed chicken tenderloins with a side of sliced sausage and carrot"></div>
    <div class="brand contacts__brand"><span class="brand__dot"></span>Brisk Ladle</div>
    <h2 class="contacts__title">CONTACTS:</h2>
    <ul class="contacts__list">
      <li>Brisk Ladle</li>
      <li>123 555 0199</li>
      <li>hello@briskladle.com.au</li>
      <li>www.briskladle.com.au</li>
      <li>facebook.com/briskladle</li>
    </ul>
  </article>

  <article class="panel cover">
    <div class="brand cover__brand"><span class="brand__dot"></span>Brisk Ladle</div>
    <p class="cover__tagline">Eat Fresh and <em>Healthy</em></p>
    <svg class="cover__photo" width="260" height="310" viewBox="0 0 260 310" role="img" aria-label="Photo of grilled salmon fillet with tomato and lettuce salad and lemon">
      <defs>
        <radialGradient id="salmonPlate" cx="45%" cy="45%" r="60%">
          <stop offset="0" stop-color="#e8894a"/>
          <stop offset="0.45" stop-color="#d8a37a"/>
          <stop offset="0.75" stop-color="#8fb25a"/>
          <stop offset="1" stop-color="#e7e2da"/>
        </radialGradient>
      </defs>
      <circle cx="215" cy="215" r="205" fill="url(#salmonPlate)" stroke="var(--navy)" stroke-width="6"/>
    </svg>
  </article>
</section>

<!-- Inside of the trifold -->
<section class="sheet sheet--inside" aria-label="Menu inside">
  <article class="panel">
    <div class="photo photo--ringed" style="width:250px;height:250px;left:-70px;top:-100px;background:radial-gradient(circle at 60% 60%, #b5693a, #8d5a2e 45%, #7fa64a 80%);" role="img" aria-label="Photo of grilled chicken and sausage with salad"></div>
    <div class="photo photo--light" style="width:104px;height:104px;left:130px;top:40px;background:radial-gradient(circle at 50% 50%, #6b3a1e, #c4863a 45%, #f2ece2 75%);" role="img" aria-label="Photo of a lean beef burger"></div>

    <div class="band band--navy" style="top:186px;">CHOOSE YOUR PROTEIN</div>
    <ul class="prices" style="top:228px;">
      <li><span>Chicken Tenderloins</span><span>$10.00</span></li>
      <li><span>Lean Beef Burger</span><span>$10.00</span></li>
      <li><span>Smoked Salmon</span><span>$10.00</span></li>
      <li><span>Grass Fed Porterhouse</span><span>$10.00</span></li>
      <li><span>Seasonal White Fish</span><span>$10.00</span></li>
    </ul>

    <div class="band band--brown" style="top:338px;">CHOOSE YOUR FLAVOUR</div>
    <ul class="flavours" style="top:380px;">
      <li>Honey Soy</li>
      <li>Harissa</li>
      <li>Italian Style</li>
      <li>Peanut Satay</li>
      <li>Mango Chili</li>
      <li>Lime &amp; Chili</li>
      <li>Vietnamese Style</li>
      <li>Teriyaki</li>
      <li>Tandoori</li>
      <li>Herb &amp; Garlic</li>
      <li>Blackbean</li>
      <li>Fajita</li>
      <li>Argentina</li>
      <li>Roast Capsicum</li>
    </ul>
  </article>

  <article class="panel">
    <div class="band band--green" style="top:86px;">CHOOSE YOUR CARBOHYDRATE</div>
    <ul class="prices" style="top:128px;">
      <li><span>Basmati Rice</span><span>$10.00</span></li>
      <li><span>Brown Rice</span><span>$10.00</span></li>
      <li><span>Sweet Potato Mash</span><span>$10.00</span></li>
      <li><span>Sweet Potato Roasted</span><span>$10.00</span></li>
      <li><span>White Potato Mash</span><span>$10.00</span></li>
      <li><span>White Potato Roasted</span><span>$10.00</span></li>
    </ul>

    <div class="band band--red" style="top:262px;">CHOOSE YOUR VEGETABLE/SALAD</div>
    <ul class="prices" style="top:304px;">
      <li><span>Steamed Vegetables (seasonal)</span><span>$10.00</span></li>
      <li><span>Greek Salad</span><span>$10.00</span></li>
      <li><span>Caesar Salad</span><span>$10.00</span></li>
    </ul>

    <div class="photo photo--light" style="width:116px;height:116px;left:14px;top:420px;background:radial-gradient(circle at 50% 50%, #6d3b2c, #b03a2e 45%, #5f8a3a 80%);" role="img" aria-label="Photo of a bean and tomato salad"></div>
    <div class="photo photo--ringed" style="width:300px;height:300px;left:110px;top:400px;background:radial-gradient(circle at 40% 40%, #f4f2ea, #9cc35a 40%, #c8402e 70%, #e7e4dc);" role="img" aria-label="Photo of a Greek salad with feta and olives"></div>
  </article>

  <article class="panel">
    <div class="photo photo--ringed" style="width:250px;height:250px;left:40px;top:-100px;background:radial-gradient(circle at 50% 60%, #f3d23e, #f7f3e6 40%, #e9e6df 80%);" role="img" aria-label="Photo of sliced boiled eggs in a bowl"></div>
    <div class="photo photo--light" style="width:92px;height:92px;left:16px;top:32px;background:radial-gradient(circle at 50% 40%, #c8302e, #f3ead8 40%, #e6dcc4);" role="img" aria-label="Photo of protein ice cream with a cherry"></div>

    <div class="band band--magenta" style="top:170px;">EXTRAS</div>
    <ul class="prices" style="top:212px;">
      <li><span>Whey Whip Protein Ice Cream</span><span>$10.00</span></li>
      <li><span>Whey Whip Protein Balls</span><span>$10.00</span></li>
      <li><span>Greek Style Yoghurt with Muesli</span><span>$10.00</span></li>
      <li><span>Roast Almond Tubs</span><span>$10.00</span></li>
      <li><span>Boiled Eggs</span><span>$10.00</span></li>
      <li><span>Avocado (Whole)</span><span>$10.00</span></li>
    </ul>

    <div class="delivery">
      <p class="delivery__head">FREE HOME DELIVERY</p>
      <p class="delivery__call">CALL US NOW TO PLACE AN ORDER</p>
      <p class="delivery__phone">ROSA: 123 555 0199</p>
    </div>
  </article>

  <h2 class="steps-title">DESIGN YOUR MEALS IN 4 EASY STEPS</h2>
</section>

</body>
</html>
```